Forking Well Buisiness card

needing a Business card for our company - Forking Well.
Forking well is co owned by Jess and Owen Marchetti (Husband and Wife)
Services Forking Well provides include:
Dietetic/nutrition Consultations, weight loss coaching programs, personal and group training, post injury rehab, health and nutrition presentations and Health Retreats.
Jess:
Accredited Practicing Dietitian & Personal trainer
Owen:
Personal trainer, rehab trainer & Strength and conditioning coach
At this stage the business cards will be made just for Jess.
She has a training studio in Armadale and Dietetics private practice in Richmond.
Mobile services are also available (i.e. meet at house or local cafe)

We need the card to look smart, modern and combine both nutrition and training.
We already have a logo which I will attach.
I was initial thinking i black background but am open to suggestions.

Target Market(s)

Health concious, People with money,

Industry/Entity Type

Nutrition

Contact Information for Business Card

Forking Well
Jess Marchetti
M: 0417 390 265
E: forkingwell@mailnest.com
W: www.forkingwell.com.au
Address:
Dietetics: Level 1, 583 Bellow Street
Richmond VIC 3121
Training: Private Studio, behind 2087 Tamsin St
ARMADALE, VIC, 3143

Requirements
Must have
• Must have logo (see attached) please not the one we use is the top left (blue and green)
please note attachment is top left (green and blue)

needs to be clear to read - the font needs to be clear and sharp and the background cannot be too busy.eg funny patterns.
Could I please see a card with a line for 'appointment time/date:' possibly on the back. Would like to see what this looks like.
Jess Marchetti's Profile (side of card) must include "Accredited Practicing Dietitian" and "Personal Trainer."
I like when the services forking well provide are in dot form.
Nice to have
• would like the card to be 2 sides
first side:
Forking well logo - Large
services forking well provides: Dietetic/nutrition Consultations, weight loss coaching programs, personal and group training, post injury rehab, health and nutrition presentations and Health Retreats.
web address
second side:
smaller logo
Details for Jess:
Accredited Practicing Dietitian
Personal Trainer
Contact Details:
M: 0417 390 265
E: forkingwell@mailnest.com
Address:
Richmond VIC 3121
ARMADALE, VIC, 3143
Should not have
• Dietetic + nutrition consultations
Should say dietetic/nutrition consultations (first letter of words in capitals please)
Please write phone number as 0417 390 265
Not: 04 17 390265
- note numbers as 4, 3, 3.

```html
<!DOCTYPE html>
<html lang="en">
<head>
<meta charset="utf-8">
<title>Forking Well – Business Card</title>
<link href="https://fonts.googleapis.com/css2?family=Cabin:ital,wght@0,400;0,600;0,700;1,600;1,700&display=swap" rel="stylesheet">
<style>
  :root {
    --brand-blue: #1b57a6;
    --brand-navy: #0d4a9c;
    --brand-green: #7dc242;
    --ink-grey: #6b6f74;
    --card-white: #ffffff;
    --card-fade: #eef1f4;
    --stage: #2b2b2b;
    --rule: #c9cdd2;
  }
  * { box-sizing: border-box; margin: 0; padding: 0; }
  html, body {
    width: 1200px; height: 900px; overflow: hidden;
    background: var(--stage);
    font-family: "Cabin", "Trebuchet MS", sans-serif;
  }
  .sheet {
    width: 1200px; height: 900px;
    display: flex; flex-direction: column; align-items: center; justify-content: center;
    gap: 40px;
  }
  .card {
    position: relative;
    width: 700px; height: 400px;
    background: linear-gradient(180deg, var(--card-white) 0%, var(--card-fade) 100%);
    overflow: hidden;
    box-shadow: 0 12px 30px rgba(0,0,0,.45);
  }
  .card__shapes { position: absolute; inset: 0; }

  /* wordmark stand-in */
  .brand { position: absolute; display: flex; align-items: center; gap: 12px; }
  .brand__dot { border-radius: 50%; border: 4px solid var(--brand-green); }
  .brand__name { color: var(--brand-blue); font-weight: 600; white-space: nowrap; }

  /* services side */
  .card--services .brand { left: 150px; top: 40px; }
  .card--services .brand__dot { width: 70px; height: 70px; }
  .card--services .brand__name { font-size: 52px; letter-spacing: -0.5px; }
  .services {
    position: absolute; left: 28px; top: 170px;
    list-style: none; color: var(--card-white);
    font-style: italic; font-weight: 700; font-size: 17px; line-height: 32px;
  }
  .services li::before {
    content: "›"; display: inline-block; width: 20px; font-style: normal; font-weight: 700;
  }
  .appointment {
    position: absolute; right: 30px; top: 262px;
    color: var(--brand-navy); font-weight: 700; font-style: italic; font-size: 17px;
  }
  .web-address {
    position: absolute; left: 30px; top: 342px;
    color: var(--brand-navy); font-weight: 700; font-style: italic; font-size: 19px;
  }

  /* profile side */
  .card--profile .brand { left: 36px; top: 40px; gap: 8px; }
  .card--profile .brand__dot { width: 42px; height: 42px; border-width: 3px; }
  .card--profile .brand__name { font-size: 30px; }
  .profile { position: absolute; left: 36px; top: 128px; }
  .profile__name { color: var(--brand-blue); font-weight: 700; font-size: 26px; line-height: 1.1; }
  .profile__role { color: var(--brand-green); font-weight: 700; font-size: 18px; line-height: 1.25; }
  .divider { position: absolute; left: 350px; top: 42px; width: 1px; height: 70px; background: var(--rule); }
  .contacts { position: absolute; left: 372px; top: 36px; list-style: none; }
  .contacts li {
    display: flex; align-items: center; gap: 10px;
    color: var(--ink-grey); font-size: 15px; line-height: 26px;
  }
  .contacts svg { width: 14px; height: 14px; fill: var(--brand-blue); flex: none; }
  .addresses { position: absolute; left: 36px; top: 250px; display: flex; gap: 10px; }
  .addresses svg { width: 14px; height: 20px; fill: var(--brand-blue); margin-top: 4px; flex: none; }
  .addresses p { color: var(--ink-grey); font-size: 15px; line-height: 26px; }
  .addresses .label { color: var(--brand-green); font-weight: 700; }
</style>
</head>
<body>
<main class="sheet">

  <!-- Profile side -->
  <section class="card card--profile" aria-label="Business card, profile side">
    <svg class="card__shapes" viewBox="0 0 700 400" aria-hidden="true">
      <polygon points="330,400 700,320 700,400" fill="var(--brand-green)"/>
      <polygon points="620,320 700,302 700,350 660,330" fill="var(--brand-navy)"/>
      <line x1="330" y1="400" x2="700" y2="320" stroke="var(--card-white)" stroke-width="3"/>
    </svg>

    <div class="brand">
      <span class="brand__dot"></span>
      <span class="brand__name">Forking Well</span>
    </div>

    <div class="profile">
      <h1 class="profile__name">Jess Marchetti</h1>
      <p class="profile__role">Accredited Practicing Dietitian</p>
      <p class="profile__role">Personal Trainer</p>
    </div>

    <span class="divider"></span>
    <ul class="contacts">
      <li><svg viewBox="0 0 14 14"><rect x="3" y="0" width="8" height="14" rx="1.5"/></svg>0417 390 265</li>
      <li><svg viewBox="0 0 14 14"><path d="M0 3h14v8H0z M0 3l7 5 7-5" /></svg>forkingwell@mailnest.com</li>
      <li><svg viewBox="0 0 14 14"><circle cx="7" cy="7" r="7"/></svg>www.forkingwell.com.au</li>
    </ul>

    <div class="addresses">
      <svg viewBox="0 0 14 20"><path d="M7 0a7 7 0 0 0-7 7c0 5 7 13 7 13s7-8 7-13a7 7 0 0 0-7-7zm0 10a3 3 0 1 1 0-6 3 3 0 0 1 0 6z"/></svg>
      <div>
        <p><span class="label">Dietetics:</span> Level 1, 583 Bellow Street Richmond VIC 3121</p>
        <p><span class="label">Training:</span> Private Studio, behind 2087 Tamsin St Armadale, VIC, 3143</p>
      </div>
    </div>
  </section>

  <!-- Services side -->
  <section class="card card--services" aria-label="Business card, services side">
    <svg class="card__shapes" viewBox="0 0 700 400" aria-hidden="true">
      <polygon points="560,105 700,105 700,240 630,240 650,195" fill="var(--brand-navy)"/>
      <polygon points="0,150 580,150 628,198 480,295 0,295" fill="var(--brand-green)" stroke="var(--card-white)" stroke-width="3"/>
    </svg>

    <div class="brand">
      <span class="brand__dot"></span>
      <span class="brand__name">Forking Well</span>
    </div>

    <ul class="services">
      <li>Dietetic/nutrition Consultations, weight loss coaching programs.</li>
      <li>Personal and group training, post injury rehab.</li>
      <li>Health and nutrition presentations and Health Retreats.</li>
    </ul>

    <p class="appointment">Your next appointment is:...</p>
    <p class="web-address">www.forkingwell.com.au</p>
  </section>

</main>
</body>
</html>
```